website for Vindoralis.de

In Naturheilzentrum VINDORALIS, the medical team using the Advanced Laboratory examines the health status of patients and each patient is treated with special care in Germany. Multi language.
The design must show mix of modern medical service.
pages :
1. Home
2. Philosophie
3.Diagnose
4. Therapie
5. Kontakt
6.über uns
7. Zentrum ( Bilder )
8.Unser Ergebnisse
9. Anfahrt

Target Market(s)

International

Industry/Entity Type

Hospital

Font styles to use
Decorative

Colors
0455a3

Requirements
Must have
• The design must show mix of modern medical service.
• Advanced Laboratory abilities.
Nice to have
• Medical Theme

```html
<!DOCTYPE html>
<html lang="de">
<head>
<meta charset="utf-8">
<title>Vindoralis – Naturheilzentrum</title>
<link rel="stylesheet" href="https://fonts.googleapis.com/css2?family=Lato:ital,wght@0,400;0,700;0,900;1,400&display=swap">
<style>
:root{
  --brand:#0455a3;
  --brand-dark:#043e7a;
  --ink:#222;
  --body:#555;
  --light:#f2f2f2;
  --white:#fff;
  --lab-navy:#062a78;
  --lab-blue:#0d5fd6;
  --lab-cyan:#4fa8ff;
  --lab-pale:#9fd0ff;
}
*{box-sizing:border-box;margin:0;padding:0}
html,body{width:1200px;height:3232px;overflow:hidden}
body{font-family:"Lato",sans-serif;color:var(--body);background:var(--white);position:relative}
.abs{position:absolute}
.center{text-align:center}

/* header + hero */
.hero-photo{left:0;top:0;width:1200px;height:661px;
  background:
    radial-gradient(ellipse 260px 330px at 180px 360px,rgba(159,208,255,.55),transparent 70%),
    radial-gradient(ellipse 300px 220px at 760px 250px,rgba(120,190,255,.45),transparent 70%),
    radial-gradient(ellipse 380px 300px at 1060px 420px,rgba(90,170,255,.40),transparent 70%),
    radial-gradient(ellipse 500px 260px at 600px 620px,rgba(4,40,130,.55),transparent 70%),
    linear-gradient(180deg,#0a2d8c 0%,#0b4fc4 22%,#1070e6 55%,#0b58cf 80%,#0a3fa8 100%)}
.brand-name{left:75px;top:24px;color:var(--white);font-size:34px;font-weight:400;letter-spacing:1px}
.contact-item{top:30px;color:var(--white);display:flex;gap:14px;align-items:flex-start}
.contact-item small{display:block;font-size:13px;font-weight:700;letter-spacing:.5px}
.contact-item strong{display:block;font-size:24px;font-weight:700;margin-top:2px}
.contact-item span.val{display:block;font-size:19px;margin-top:4px}
.main-nav{left:0;top:112px;width:1200px;height:56px;background:var(--white);display:flex;align-items:center;padding-left:83px}
.main-nav a{font-size:13px;font-weight:700;color:#222;text-decoration:none;margin-right:40px;letter-spacing:.2px}
.main-nav a.active{color:var(--brand)}
.hero-title{left:0;width:1200px;top:318px;color:var(--white);font-size:54px;font-weight:900;text-align:center}
.hero-sub{left:0;width:1200px;top:390px;color:var(--white);font-size:22px;text-align:center;line-height:30px}
.slider-arrows{left:571px;top:604px;display:flex;gap:12px}
.slider-arrows span{width:24px;height:24px;border:1.5px solid rgba(255,255,255,.8);border-radius:50%;display:block}

/* section headings */
.sec-title{left:0;width:1200px;font-size:30px;font-weight:700;color:var(--ink);text-align:center}
.rule{width:96px;height:4px;background:var(--brand);left:552px}
.para{font-size:15px;line-height:28px;color:var(--body)}
.btn{background:var(--brand);color:var(--white);font-size:14px;font-weight:700;display:flex;align-items:center;justify-content:center;letter-spacing:.5px}

/* services */
.services-bg{left:0;top:1038px;width:1200px;height:483px;background:var(--light)}
.service{width:330px;text-align:center}
.service .ring{width:112px;height:112px;border:3px solid var(--brand);border-radius:50%;margin:0 auto;display:flex;align-items:center;justify-content:center;background:var(--white)}
.service h3{color:var(--brand);font-size:17px;font-weight:700;margin-top:24px}
.service p{font-size:14px;line-height:20px;margin-top:6px;color:#444}

/* about */
.about-photo{left:75px;top:1575px;width:511px;height:329px;
  background:
    radial-gradient(ellipse 120px 150px at 110px 150px,rgba(225,232,242,.55),transparent 70%),
    radial-gradient(ellipse 90px 200px at 300px 130px,rgba(210,225,245,.55),transparent 70%),
    radial-gradient(ellipse 160px 120px at 440px 80px,rgba(150,175,210,.45),transparent 70%),
    linear-gradient(110deg,#1b2740 0%,#4a5d80 35%,#8a9cb8 60%,#3e5072 100%)}
.about-title{left:616px;top:1563px;font-size:30px;font-weight:700;color:var(--ink)}

/* testimonials */
.testi-bg{left:0;top:1960px;width:1200px;height:450px;
  background:
    radial-gradient(ellipse 260px 200px at 200px 120px,rgba(110,160,240,.35),transparent 70%),
    radial-gradient(ellipse 300px 220px at 1000px 300px,rgba(110,160,240,.30),transparent 70%),
    linear-gradient(100deg,#0b3480,#0a4db0 45%,#0c3b8c 100%)}
.testi-title{left:0;width:1200px;top:2007px;color:var(--white);font-size:30px;font-weight:700;text-align:center}
.quote{left:130px;width:940px;top:2098px;color:var(--white);font-size:15px;line-height:27px;font-style:italic;text-align:center}
.avatar{left:564px;top:2198px;width:73px;height:73px;border-radius:50%;border:4px solid var(--white);background:linear-gradient(#dfe5ec,#9fb0c4)}
.testi-name{left:0;width:1200px;top:2292px;color:var(--white);font-size:14px;font-weight:700;text-align:center}
.dots{left:566px;top:2346px;display:flex;gap:6px}
.dots span{width:10px;height:10px;border-radius:50%;background:var(--white)}
.dots span.off{background:transparent;border:1.5px solid var(--white)}

/* blog */
.post{width:340px}
.post .thumb{height:183px;width:330px}
.post h4{color:var(--brand);font-size:17px;font-weight:900;margin-top:26px}
.post p{font-size:14px;line-height:21px;color:#333;margin-top:6px}
.post .meta{font-size:13px;color:var(--brand);font-weight:700;margin-top:16px}
.thumb-dna{background:
    radial-gradient(ellipse 90px 80px at 80px 80px,rgba(120,230,255,.6),transparent 70%),
    radial-gradient(ellipse 70px 110px at 220px 110px,rgba(230,240,250,.55),transparent 70%),
    linear-gradient(120deg,#08224a,#1c5a9a 55%,#0a2a52)}
.thumb-steth{background:
    radial-gradient(ellipse 110px 70px at 170px 70px,rgba(170,190,210,.7),transparent 70%),
    radial-gradient(ellipse 70px 60px at 70px 130px,rgba(220,190,170,.6),transparent 70%),
    linear-gradient(120deg,#f2f5f8,#c7d2de 55%,#eef2f6)}
.thumb-micro{background:
    radial-gradient(ellipse 110px 120px at 70px 90px,rgba(226,170,150,.9),transparent 70%),
    radial-gradient(ellipse 90px 110px at 230px 110px,rgba(40,48,60,.8),transparent 70%),
    linear-gradient(120deg,#d8b0a0,#9ba4b0 50%,#e6eef6)}

/* footer */
.footer-bg{left:0;top:2942px;width:1200px;height:290px;background:var(--light)}
.foot-brand{left:75px;top:2996px;font-size:32px;color:var(--brand-dark);letter-spacing:1px}
.foot-copy{left:75px;top:3066px;font-size:12px;line-height:17px;color:#444}
.social{left:75px;top:3132px;display:flex;gap:18px}
.social span{width:16px;height:16px;border-radius:50%;background:#555;display:block}
.foot-head{top:2994px;font-size:14px;font-weight:900;color:var(--brand-dark);letter-spacing:.5px}
.foot-list{font-size:14px;line-height:28px;color:#333;list-style:none}
.foot-contact{left:644px;top:3022px;font-size:14px;color:#333}
.foot-contact li{list-style:none;display:flex;gap:16px;align-items:flex-start;line-height:19px;margin-bottom:9px}
.foot-contact li svg{flex:none;margin-top:2px}
.sub-text{left:885px;top:3022px;width:240px;font-size:14px;line-height:19px;color:#333}
.email-field{left:885px;top:3080px;width:239px;height:39px;background:var(--white);font-size:12px;color:#333;display:flex;align-items:center;padding-left:14px}
</style>
</head>
<body>

<div class="abs hero-photo" role="img" aria-label="Laboratory scientist in mask beside a glowing DNA double helix and molecular structures, tinted blue"></div>
<div class="abs brand-name">VINDORALIS</div>

<div class="abs contact-item" style="left:622px">
  <svg width="22" height="22" viewBox="0 0 24 24"><path fill="#fff" d="M6.6 10.8a15.1 15.1 0 0 0 6.6 6.6l2.2-2.2c.3-.3.7-.4 1-.2 1.1.4 2.3.6 3.6.6.6 0 1 .4 1 1V20c0 .6-.4 1-1 1A17 17 0 0 1 3 4c0-.6.4-1 1-1h3.5c.6 0 1 .4 1 1 0 1.3.2 2.5.6 3.6.1.3 0 .7-.2 1z"/></svg>
  <div><small>CALL US:</small><strong>1-800-555-0142</strong></div>
</div>
<div class="abs contact-item" style="left:874px">
  <svg width="24" height="20" viewBox="0 0 24 20"><path fill="#fff" d="M2 2h20c.6 0 1 .4 1 1v14c0 .6-.4 1-1 1H2c-.6 0-1-.4-1-1V3c0-.6.4-1 1-1zm10 8.5L3 4.5V6l9 6 9-6V4.5z"/></svg>
  <div><small>EMAIL US:</small><span class="val">info@vindoralis-mail.de</span></div>
</div>

<nav class="abs main-nav">
  <a class="active">HOME</a><a>PHILOSOPHIE</a><a>DIAGNOSE</a><a>THERAPIE</a><a>KONTAKT</a><a>ÜBER UNS</a><a>ZENTRUM ( BILDER )</a><a>UNSER ERGEBNISSE</a><a>ANFAHRT</a>
</nav>

<h1 class="abs hero-title">WELCOME TO VINDORALIS</h1>
<p class="abs hero-sub">Our medical team uses the Advanced Laboratory examines the health status of<br>patients and each patient is treated with special care in Germany.</p>
<div class="abs slider-arrows"><span></span><span></span></div>

<!-- welcome -->
<h2 class="abs sec-title" style="top:706px">WELCOME TO OUR WEBSITE</h2>
<div class="abs rule" style="top:763px"></div>
<p class="abs para center" style="left:60px;width:1080px;top:788px">Aliquam molestie, mi et imperdiet euismod, dui purus auctor tellus, et interdum lacus lectus et ante. Sed accumsan sollicitudin sapien, sit<br>amet adipiscing turpis gravida ac. In congue, neque ac lobortis volutpat, libero mauris varius mi, vitae suscipit ipsum ligula vitae risus.<br>Duis aliquam nibh a dui iaculis viverra id a velit. Vivamus egestas risus in magna varius commodo. Sed semper viverra egestas.<br>Etiam pretium porttitor lectus, vel ornare neque porta volutpat.</p>
<div class="abs btn" style="left:510px;top:933px;width:179px;height:43px">READ MORE</div>

<!-- services -->
<div class="abs services-bg"></div>
<h2 class="abs sec-title" style="top:1083px">WHAT WE DO</h2>
<div class="abs rule" style="top:1140px"></div>

<div class="abs service" style="left:91px;top:1195px">
  <div class="ring"><svg width="48" height="44" viewBox="0 0 48 44"><rect x="16" y="2" width="16" height="8" rx="2" fill="none" stroke="#333" stroke-width="3"/><rect x="3" y="9" width="42" height="32" rx="4" fill="#333"/><path d="M20 16h8v6h6v8h-6v6h-8v-6h-6v-8h6z" fill="#fff"/></svg></div>
  <h3>PHILOSOPHIE</h3>
  <p>Aliquam molestie, mi et imperdiet euismod,<br>dui purus auctor tellus, et interdum lacus<br>lectus et ante lobortis turpis in<br>odio blandit ac..</p>
</div>
<div class="abs service" style="left:436px;top:1195px">
  <div class="ring"><svg width="46" height="50" viewBox="0 0 46 50"><rect x="20" y="2" width="9" height="22" rx="2" transform="rotate(20 24 13)" fill="#333"/><circle cx="22" cy="30" r="8" fill="none" stroke="#333" stroke-width="3"/><path d="M30 20c8 4 10 14 4 22" fill="none" stroke="#333" stroke-width="3"/><rect x="8" y="42" width="32" height="5" rx="1" fill="#333"/></svg></div>
  <h3>DIAGNOSE</h3>
  <p>Aliquam molestie, mi et imperdiet euismod,<br>dui purus auctor tellus, et interdum lacus<br>lectus et ante lobortis turpis in<br>odio blandit ac..</p>
</div>
<div class="abs service" style="left:791px;top:1195px">
  <div class="ring"><svg width="50" height="44" viewBox="0 0 50 44"><circle cx="20" cy="8" r="6" fill="#333"/><rect x="4" y="20" width="42" height="7" rx="2" fill="#333"/><rect x="8" y="27" width="4" height="14" fill="#333"/><rect x="38" y="27" width="4" height="14" fill="#333"/><path d="M30 18l8-8 4 4" fill="none" stroke="#333" stroke-width="3"/></svg></div>
  <h3>THERAPIE</h3>
  <p>Aliquam molestie, mi et imperdiet euismod,<br>dui purus auctor tellus, et interdum lacus<br>lectus et ante lobortis turpis in<br>odio blandit ac..</p>
</div>

<!-- about -->
<div class="abs about-photo" role="img" aria-label="Female researcher in surgical cap looking at a glowing DNA double helix in a laboratory"></div>
<h2 class="abs about-title">ABOUT VINDORALIS</h2>
<div class="abs" style="left:616px;top:1627px;width:96px;height:4px;background:var(--brand)"></div>
<p class="abs para" style="left:616px;top:1650px;width:520px;font-size:14px;line-height:26px">Aliquam molestie, mi et imperdiet euismod, dui purus auctor tellus,<br>et interdum lacus lectus et ante. Sed accumsan sollicitudin sapien, sit amet<br>adipiscing turpis gravida ac. In congue, neque ac lobortis volutpat, libero<br>mauris varius mi, vitae suscipit ipsum ligula vitae risus. Duis aliquam nibh a<br>dui iaculis viverra id a velit. Vivamus egestas risus in magna varius<br>commodo. Sed semper viverra egestas pretium porttitor lectus, vel ornare<br>neque porta volutpat.</p>
<div class="abs btn" style="left:616px;top:1861px;width:179px;height:43px">READ MORE</div>

<!-- testimonials -->
<div class="abs testi-bg" role="img" aria-label="Laboratory team working with microscopes and test tubes, tinted blue"></div>
<h2 class="abs testi-title">TESTIMONIALS</h2>
<div class="abs rule" style="top:2062px;background:var(--white)"></div>
<p class="abs quote">" Aliquam molestie, mi et imperdiet euismod, dui purus auctor tellus, et interdum lacus lectus et ante. Sed accumsan<br>sollicitudin sapien, sit amet adipiscing turpis gravida ac. In congue, neque ac lobortis volutpat, libero mauris varius mi, vitae suscipit<br>ipsum ligula vitae risus. Duis aliquam nibh a dui iaculis viverra id a velit..."</p>
<div class="abs avatar" role="img" aria-label="Portrait of the reviewer"></div>
<div class="abs testi-name">-NAME HEADING</div>
<div class="abs dots"><span></span><span class="off"></span><span></span><span></span></div>

<!-- blog -->
<h2 class="abs sec-title" style="top:2453px">BLOG POSTS</h2>
<div class="abs rule" style="top:2510px"></div>

<article class="abs post" style="left:75px;top:2557px">
  <div class="thumb thumb-dna" role="img" aria-label="Scientist in lab coat holding a glowing DNA model"></div>
  <h4>NAM FERMENTUM VESTIBULUM</h4>
  <p>Aliquam molestie, mi et imperdiet euismod,<br>dui purus auctor tellus, et interdum lacus<br>lectus et ante lobortis turpis in &nbsp;odio blandit ac..</p>
  <div class="meta">Jan 20, 2018 &nbsp;|&nbsp; By Admin</div>
</article>
<article class="abs post" style="left:433px;top:2557px">
  <div class="thumb thumb-steth" role="img" aria-label="Doctor holding a stethoscope with medical interface icons"></div>
  <h4>NAM FERMENTUM VESTIBULUM</h4>
  <p>Aliquam molestie, mi et imperdiet euismod,<br>dui purus auctor tellus, et interdum lacus<br>lectus et ante lobortis turpis in &nbsp;odio blandit ac..</p>
  <div class="meta">Jan 20, 2018 &nbsp;|&nbsp; By Admin</div>
</article>
<article class="abs post" style="left:795px;top:2557px">
  <div class="thumb thumb-micro" role="img" aria-label="Researcher looking into a laboratory microscope"></div>
  <h4>NAM FERMENTUM VESTIBULUM</h4>
  <p>Aliquam molestie, mi et imperdiet euismod,<br>dui purus auctor tellus, et interdum lacus<br>lectus et ante lobortis turpis in &nbsp;odio blandit ac..</p>
  <div class="meta">Jan 20, 2018 &nbsp;|&nbsp; By Admin</div>
</article>

<!-- footer -->
<footer>
<div class="abs footer-bg"></div>
<div class="abs foot-brand">VINDORALIS</div>
<p class="abs foot-copy">Copyright © 2018. Company Name<br>All Right Reserved</p>
<div class="abs social"><span></span><span></span><span></span><span></span><span></span><span></span></div>

<h5 class="abs foot-head" style="left:342px">SITE MAP</h5>
<ul class="abs foot-list" style="left:342px;top:3016px"><li>Home</li><li>Philosophie</li><li>Diagnose</li><li>Therapie</li><li>Kontakt</li></ul>
<ul class="abs foot-list" style="left:476px;top:3016px"><li>über uns</li><li>Zentrum ( Bilder )</li><li>Unser Ergebnisse</li><li>Anfahrt</li></ul>

<h5 class="abs foot-head" style="left:644px">CONTACT ADDRESS</h5>
<ul class="abs foot-contact">
  <li style="display:block">4120 Lindenweg<br>Road,Harbourton, D07 31KL</li>
  <li><svg width="14" height="14" viewBox="0 0 24 24"><path fill="#444" d="M6.6 10.8a15.1 15.1 0 0 0 6.6 6.6l2.2-2.2c.3-.3.7-.4 1-.2 1.1.4 2.3.6 3.6.6.6 0 1 .4 1 1V20c0 .6-.4 1-1 1A17 17 0 0 1 3 4c0-.6.4-1 1-1h3.5c.6 0 1 .4 1 1 0 1.3.2 2.5.6 3.6.1.3 0 .7-.2 1z"/></svg>1-800-555-0142</li>
  <li><svg width="14" height="12" viewBox="0 0 24 20"><path fill="#444" d="M2 2h20c.6 0 1 .4 1 1v14c0 .6-.4 1-1 1H2c-.6 0-1-.4-1-1V3c0-.6.4-1 1-1zm10 8.5L3 4.5V6l9 6 9-6V4.5z"/></svg>info@vindoralis-mail.de</li>
  <li><svg width="12" height="16" viewBox="0 0 12 16"><path fill="#444" d="M6 0a6 6 0 0 1 6 6c0 4.5-6 10-6 10S0 10.5 0 6a6 6 0 0 1 6-6zm0 3.5a2.5 2.5 0 1 0 0 5 2.5 2.5 0 0 0 0-5z"/></svg>Map Direction</li>
</ul>

<h5 class="abs foot-head" style="left:885px">EMAIL SUBSCRIBE</h5>
<p class="abs sub-text">Vestibulum ante ipsum primis in faucibus orci luctus..</p>
<div class="abs email-field">Enter Email Address</div>
<div class="abs btn" style="left:1036px;top:3130px;width:88px;height:36px;font-size:13px">SIGN UP</div>
</footer>

</body>
</html>
```